Business Postcard to attract business listings on directory

We need a postcard that professionally and excitedly highlights the benefits of getting listed on our local business directory.

Our local business directory combines a Quarterly direct mail piece a LOCAL discount card, which means no coupons for people to remember to use, and the power of an online directory and the benefits of local SEO.

Colorful, Vector/Images and Bold text a must

Target Market(s)

Local business, all industrys that service the public, retail,food, construction,plumbing etc.

Industry/Entity Type

Business Directory

Font styles to use
Other font styles liked:
• Calibri,Verdana

Requirements
Must have
• High Quality Graphics
• Vector Icons
• Vibrant Professional Colors
• Place for my contact details
Nice to have
• Some kind of business guy, Cartoonish maybe flying or "exploding" with new business sales
Should not have
• Excessive Blank Space

```html
<!DOCTYPE html>
<html lang="en">
<head>
<meta charset="utf-8">
<title>Local Business Listings Postcard</title>
<link rel="stylesheet" href="https://fonts.googleapis.com/css2?family=Oswald:wght@500;600;700&family=Montserrat:wght@500;700;800&family=Roboto+Slab:wght@800&display=swap">
<style>
  :root{
    --navy:#0f3f8f;
    --royal:#1d4fa6;
    --orange:#f5891f;
    --amber:#f7a21b;
    --sky-top:#1f7fc1;
    --sky-mid:#3fb3d6;
    --sky-low:#e9f6fb;
    --road:#5f5f66;
    --line:#f6c32a;
    --white:#ffffff;
    --stamp:#d9d3cf;
    --page:#e7e7e7;
  }
  *{box-sizing:border-box;margin:0;padding:0}
  html,body{width:1200px;height:1200px;overflow:hidden;background:var(--page)}
  .canvas{position:relative;width:1200px;height:1200px}
  .card{position:absolute;left:210px;width:780px;height:565px;overflow:hidden;box-shadow:0 6px 18px rgba(0,0,0,.25)}
  /* FRONT */
  .front{top:20px;background:linear-gradient(180deg,var(--sky-top) 0%,var(--sky-mid) 28%,var(--sky-low) 58%,var(--white) 75%)}
  .front__head{position:absolute;left:30px;top:22px;width:560px;font-family:'Oswald',sans-serif;color:var(--white);text-transform:uppercase;line-height:1}
  .front__line1{font-size:36px;font-weight:600;letter-spacing:-.3px;white-space:nowrap}
  .front__line2{font-size:52px;font-weight:700;letter-spacing:-.8px;margin-top:4px;white-space:nowrap}
  .front__line2 .accent{color:var(--amber)}
  .front__url{position:absolute;left:32px;top:130px;font-family:'Montserrat',sans-serif;font-weight:800;font-size:20px;letter-spacing:11px;color:var(--white);white-space:nowrap}
  .front__copy{position:absolute;left:20px;top:172px;width:570px;text-align:center;font-family:'Montserrat',sans-serif;font-weight:500;color:var(--navy);font-size:18px;line-height:1.35}
  .front__copy b{font-weight:800}
  .front__copy p{margin-bottom:8px}
  .front__hero{position:absolute;right:14px;top:30px;width:160px;height:330px;border-radius:40px;background:linear-gradient(180deg,#f28a2a 0%,#3a3f4a 45%,#cfd3d8 100%);opacity:.9}
  .front__town{position:absolute;left:0;bottom:30px;width:100%;height:150px;background:linear-gradient(180deg,#c9d3db 0%,#e8823a 55%,#2d5aa8 100%)}
  .front__road{position:absolute;left:0;bottom:0;width:100%;height:30px;background:var(--road)}
  .front__road::after{content:"";position:absolute;left:0;right:0;top:13px;height:4px;background:repeating-linear-gradient(90deg,var(--line) 0 24px,transparent 24px 48px)}
  /* BACK */
  .back{top:615px;background:var(--white)}
  .back__edge{position:absolute;inset:0}
  .back__panel{position:absolute;left:0;top:0;width:440px;height:100%;padding:20px 0 0 30px;font-family:'Montserrat',sans-serif;color:var(--white)}
  .benefits__kicker{display:flex;align-items:center;gap:10px;color:var(--orange);font-weight:700;font-size:21px;letter-spacing:1px;margin-left:4px}
  .benefits__kicker::before,.benefits__kicker::after{content:"";width:62px;height:3px;background:var(--orange)}
  .benefits__title{margin-top:2px;width:340px;height:44px;background:var(--orange);clip-path:polygon(0 0,88% 0,100% 100%,0 100%);font-family:'Roboto Slab',serif;font-weight:800;font-size:28px;letter-spacing:1px;line-height:44px;padding-left:44px}
  .benefits{list-style:none;margin-top:12px;font-size:18px;line-height:1.2}
  .benefits li{position:relative;padding-left:32px;margin-bottom:5px}
  .benefits li b{font-weight:800}
  .benefits svg{position:absolute;left:0;top:1px;width:20px;height:20px}
  .call{display:flex;align-items:center;gap:8px;margin:10px 0 0 22px;width:340px;height:42px;border-radius:21px;background:var(--orange);font-family:'Oswald',sans-serif;font-weight:600;font-style:italic;font-size:24px;color:var(--white);padding-left:4px}
  .call__icon{width:34px;height:34px;border-radius:50%;background:var(--white);display:flex;align-items:center;justify-content:center}
  .sender{margin:8px 0 0 20px;text-align:center;width:340px;font-size:16px;line-height:1.3}
  .sender__name{display:flex;align-items:center;justify-content:center;gap:8px;font-weight:800;font-size:18px}
  .sender__name::before{content:"";width:18px;height:18px;border-radius:50%;background:var(--orange)}
  .sender b{font-weight:800}
  .stamp{position:absolute;right:40px;top:28px;width:118px;height:132px;background:var(--stamp);border:5px dotted var(--white);outline:3px solid var(--stamp)}
</style>
</head>
<body>
<main class="canvas">
  <section class="card front" aria-label="Postcard front">
    <div class="front__head">
      <div class="front__line1">Boost your online presence with</div>
      <div class="front__line2"><span class="accent">Local</span> Business Listings</div>
    </div>
    <div class="front__url">www.TownListingHub.net</div>
    <div class="front__copy">
      <p>Get found where <b>YOUR shoppers</b> are searching</p>
      <p>Shoppers are increasingly turning to the web,<br>according to <b>MarketPulse's 5th Annual Local</b><br>Search Usage Study.</p>
      <p>Shoppers are <b>SEARCHING locally</b> to buy<br>in-store and then deciding to purchase.</p>
    </div>
    <div class="front__hero" role="img" aria-label="Cartoon businessman flying upward on a jetpack"></div>
    <div class="front__town" role="img" aria-label="Colourful town street of shops and houses with location pins"></div>
    <div class="front__road"></div>
  </section>

  <section class="card back" aria-label="Postcard back">
    <svg class="back__edge" viewBox="0 0 780 565" preserveAspectRatio="none" aria-hidden="true">
      <path d="M0 0 H400 C470 120 470 420 440 565 H0 Z" fill="var(--royal)"/>
      <path d="M400 0 H420 C500 140 505 420 480 565 H440 C470 420 470 120 400 0 Z" fill="var(--amber)"/>
    </svg>
    <div class="back__panel">
      <div class="benefits__kicker">BENEFITS</div>
      <div class="benefits__title">OF LISTING</div>
      <ul class="benefits">
        <li><svg viewBox="0 0 22 22"><circle cx="11" cy="11" r="11" fill="var(--amber)"/><path d="M6 11.5l3.5 3.5L16 8" stroke="#fff" stroke-width="2.6" fill="none" stroke-linecap="round"/></svg><b>MORE</b> FOOT TRAFFIC</li>
        <li><svg viewBox="0 0 22 22"><circle cx="11" cy="11" r="11" fill="var(--amber)"/><path d="M6 11.5l3.5 3.5L16 8" stroke="#fff" stroke-width="2.6" fill="none" stroke-linecap="round"/></svg>Quarterly Mailing<br>To <b>10,000 local shoppers</b></li>
        <li><svg viewBox="0 0 22 22"><circle cx="11" cy="11" r="11" fill="var(--amber)"/><path d="M6 11.5l3.5 3.5L16 8" stroke="#fff" stroke-width="2.6" fill="none" stroke-linecap="round"/></svg>Desktop &amp; Mobile<br><b>optimized online listing</b></li>
        <li><svg viewBox="0 0 22 22"><circle cx="11" cy="11" r="11" fill="var(--amber)"/><path d="M6 11.5l3.5 3.5L16 8" stroke="#fff" stroke-width="2.6" fill="none" stroke-linecap="round"/></svg><b>Show up</b><br>in Search Engine Results</li>
        <li><svg viewBox="0 0 22 22"><circle cx="11" cy="11" r="11" fill="var(--amber)"/><path d="M6 11.5l3.5 3.5L16 8" stroke="#fff" stroke-width="2.6" fill="none" stroke-linecap="round"/></svg><b>List Active</b> Coupons &amp; Deals</li>
        <li><svg viewBox="0 0 22 22"><circle cx="11" cy="11" r="11" fill="var(--amber)"/><path d="M6 11.5l3.5 3.5L16 8" stroke="#fff" stroke-width="2.6" fill="none" stroke-linecap="round"/></svg><b>Connect Direct</b> With Shoppers</li>
        <li><svg viewBox="0 0 22 22"><circle cx="11" cy="11" r="11" fill="var(--amber)"/><path d="M6 11.5l3.5 3.5L16 8" stroke="#fff" stroke-width="2.6" fill="none" stroke-linecap="round"/></svg><b>Support Local Shoppers</b><br>with the <b>LOCAL</b> Discount Card</li>
        <li><svg viewBox="0 0 22 22"><circle cx="11" cy="11" r="11" fill="var(--amber)"/><path d="M6 11.5l3.5 3.5L16 8" stroke="#fff" stroke-width="2.6" fill="none" stroke-linecap="round"/></svg>Dedicated Account Manager<br>Handles <b>everything</b> for you</li>
      </ul>
      <div class="call">
        <span class="call__icon"><svg width="20" height="20" viewBox="0 0 24 24"><path d="M6.6 10.8a15 15 0 006.6 6.6l2.2-2.2a1 1 0 011-.25 11.4 11.4 0 003.6.6 1 1 0 011 1V20a1 1 0 01-1 1A17 17 0 013 4a1 1 0 011-1h3.5a1 1 0 011 1 11.4 11.4 0 00.6 3.6 1 1 0 01-.25 1z" fill="var(--royal)"/></svg></span>
        Call Us: 1 555 014 2290
      </div>
      <div class="sender">
        <div class="sender__name">Northfield Mail Partners</div>
        P.O Box <b>418</b>, Millbrook, CT <b>06999</b>
      </div>
    </div>
    <div class="stamp" aria-label="Stamp area"></div>
  </section>
</main>
</body>
</html>
```